Online eyewear company needs a couple Sign-In and Product Review page designs

We sell prescription glasses starting at $99 with Free Shipping. We have over 300 different styles and colors.Our website is under construction and we need an amazing Sign-In and Product Review Pages to help finish things off. Our brand is called VESKA and our website is called VESKAEYEWEAR.COM.

We need 5 simple sign-in and product review pages to help finish our website. Sample pages attached

We need the pages to go in order

Quick Checkout review
Sign-In
Prescription
Shipping & Payment
Final Review

Target Market(s)

20-50 that wears glasses

Industry/Entity Type

Eyewear

Colors
ffffff
919191
eaeaea
d3d3d3
dddddd
b7b7b7
000000
3176b5

Requirements
Must have
• Simple, creative, original. Must not be exactly like the photos attached. They're just templete of our casual, simple style.
• We need the pages to go in order
• Quick Checkout review
• Sign-In
• Prescription
• Shipping & Payment
• Final Review
Should not have
• Must not look exactly like the photos attached.

```html
<!DOCTYPE html>
<html lang="en">
<head>
<meta charset="utf-8">
<title>Sign In</title>
<link rel="stylesheet" href="https://fonts.googleapis.com/css2?family=Oswald:wght@500;700&family=Poppins:ital,wght@0,400;0,600;0,700;1,400&display=swap">
<style>
  :root {
    --brand-blue: #3176b5;
    --brand-blue-deep: #2a68a3;
    --brand-blue-light: #4a8cc6;
    --white: #ffffff;
    --panel-bg: #f2f6fa;
    --text-grey: #919191;
    --text-dark-grey: #7a7a7a;
    --field-shadow: rgba(0, 0, 0, 0.06);
  }
  * { box-sizing: border-box; margin: 0; padding: 0; }
  html, body { width: 1200px; height: 450px; overflow: hidden; }
  body { font-family: "Poppins", sans-serif; background: var(--panel-bg); }

  .signin-page { position: relative; width: 1200px; height: 450px; }

  .hero {
    position: absolute; left: 0; top: 0; width: 600px; height: 450px; overflow: hidden;
    background: linear-gradient(160deg, var(--brand-blue-deep) 0%, var(--brand-blue) 55%, var(--brand-blue-light) 100%);
  }
  .hero__photo {
    position: absolute; left: 240px; top: 0; width: 360px; height: 450px;
    background: radial-gradient(ellipse at 45% 45%, rgba(30, 80, 130, 0.45) 0%, rgba(49, 118, 181, 0) 70%);
  }
  .hero__backdrop-title {
    position: absolute; left: -4px; top: 250px;
    font-family: "Oswald", sans-serif; font-weight: 700; font-size: 197px;
    line-height: 1; color: rgba(255, 255, 255, 0.1);
    white-space: nowrap;
  }
  .hero__title {
    position: absolute; left: 26px; top: 322px;
    font-family: "Oswald", sans-serif; font-weight: 700; font-size: 92px;
    line-height: 1; letter-spacing: 1px; color: var(--white);
    white-space: nowrap;
  }

  .signup {
    position: absolute; left: 638px; top: 30px; width: 540px;
  }
  .signup__heading {
    font-family: "Oswald", sans-serif; font-weight: 500; font-size: 34px;
    line-height: 1.2; color: var(--brand-blue); letter-spacing: 0.3px;
  }
  .signup__form { margin-top: 23px; display: flex; flex-direction: column; align-items: flex-start; }
  .field {
    width: 500px; height: 47px; border: none; background: var(--white);
    box-shadow: 0 2px 6px var(--field-shadow);
    font-family: "Poppins", sans-serif; font-size: 9.5px; color: var(--text-dark-grey);
    padding: 0 18px; margin-bottom: 17px; outline: none;
  }
  .field::placeholder { color: var(--text-dark-grey); }
  .field:last-of-type { margin-bottom: 20px; }
  .button-primary {
    width: 201px; height: 47px; border: none; background: var(--brand-blue);
    color: var(--white); font-family: "Poppins", sans-serif; font-weight: 700;
    font-size: 10px; letter-spacing: 0.1px; box-shadow: 0 2px 6px var(--field-shadow);
  }
  .signup__legal {
    margin-top: 27px; font-size: 10.5px; color: var(--text-grey); white-space: nowrap;
  }
  .signup__legal strong { font-weight: 600; color: var(--text-dark-grey); }
  .signup__login {
    display: inline-block; margin-top: 14px; font-size: 12px; font-style: italic;
    color: var(--brand-blue); text-decoration: underline; text-underline-offset: 3px;
  }
</style>
</head>
<body>
  <main class="signin-page">
    <section class="hero">
      <div class="hero__photo" role="img" aria-label="Photo of a smiling man in glasses talking on his phone, tinted blue"></div>
      <div class="hero__backdrop-title" aria-hidden="true">SIGN IN</div>
      <h1 class="hero__title">SIGN IN</h1>
    </section>

    <section class="signup">
      <h2 class="signup__heading">NICE TO MEET YOU!</h2>
      <form class="signup__form">
        <input class="field" type="text" placeholder="First and last name">
        <input class="field" type="email" placeholder="Email Address">
        <input class="field" type="password" placeholder="Password">
        <button class="button-primary" type="button">CREATE ACCOUNT AND CONDTINUE</button>
      </form>
      <p class="signup__legal">By creating account, you agree to the <strong>Terms of Use</strong>,<strong>Privancy Poilcy</strong>, and <strong>Notice of Privacy Pratices</strong></p>
      <a class="signup__login" href="#">I Already have an account</a>
    </section>
  </main>
</body>
</html>
```